Tending Our Garden eBook Cover Design

I want to deisgn a cover for my eBook (FRONT COVER) and the title is:

What I Grew From a Single Spark. And Why It Matters
By KT Dorran

TITLE CHANGED TO: UNDER THE WILLOW TREE; WHERE I FOUND MY QUIET STRENGTH AND WHERE YOU MIGHT TOO

The color palette is attached. Along with some photos options of me. Along with the ebook in WORD Document. My website is www.KTDorranLive.example. You can use a different color palette if you think it is best

Target Market(s)

women who look to build a personal brand

Industry/Entity Type

health and wellness

Requirements
Must have
• the title
Nice to have
• use my picture on the cover; but that is optional
Should not have
• any men

```html
<!DOCTYPE html>
<html lang="en">
<head>
<meta charset="utf-8">
<title>Under the Willow Tree – KT Dorran</title>
<link rel="stylesheet" href="https://fonts.googleapis.com/css2?family=Oswald:wght@400;500;700&display=swap">
<style>
  :root {
    --cover-blush: #f8d3c4;
    --title-wine: #652b2c;
    --title-rose: #c8737c;
    --portrait-dark: #231a1d;
    --portrait-red: #d5312b;
  }
  html, body {
    margin: 0;
    padding: 0;
    width: 800px;
    height: 1200px;
    overflow: hidden;
    background: var(--cover-blush);
  }
  .book-cover {
    display: block;
    width: 800px;
    height: 1200px;
    background: var(--cover-blush);
  }
  .title-line {
    font-family: "Oswald", "Arial Narrow", sans-serif;
  }
  .title-line--accent {
    fill: var(--title-wine);
    font-weight: 700;
  }
  .title-line--feature {
    fill: var(--title-rose);
    font-weight: 500;
  }
  .author-byline {
    font-family: "Oswald", "Arial Narrow", sans-serif;
    font-weight: 700;
    fill: var(--title-rose);
  }
  .portrait-ring {
    fill: var(--title-rose);
  }
</style>
</head>
<body>
<svg class="book-cover" viewBox="0 0 800 1200" xmlns="http://www.w3.org/2000/svg">
  <defs>
    <linearGradient id="portrait-tones" x1="0" y1="0" x2="0" y2="1">
      <stop offset="0" stop-color="var(--portrait-dark)"/>
      <stop offset="0.62" stop-color="#3a2a2a"/>
      <stop offset="1" stop-color="var(--portrait-red)"/>
    </linearGradient>
  </defs>

  <text class="title-line title-line--accent" x="55" y="122" font-size="102"
        textLength="701" lengthAdjust="spacingAndGlyphs">UNDER THE WILLOW TREE;</text>

  <text class="title-line title-line--feature" x="55" y="281" font-size="175"
        textLength="400" lengthAdjust="spacingAndGlyphs">WHERE I F</text>
  <g class="author-portrait">
    <circle class="portrait-ring" cx="530" cy="214" r="72"/>
    <circle cx="530" cy="214" r="62" fill="url(#portrait-tones)"
            role="img" aria-label="Portrait photo of the author, KT Dorran"/>
  </g>
  <text class="title-line title-line--feature" x="606" y="281" font-size="175"
        textLength="150" lengthAdjust="spacingAndGlyphs">UND</text>

  <text class="title-line title-line--feature" x="55" y="527" font-size="290"
        textLength="701" lengthAdjust="spacingAndGlyphs">MY QUIET</text>

  <text class="title-line title-line--feature" x="55" y="811" font-size="340"
        textLength="701" lengthAdjust="spacingAndGlyphs">STRENGTH</text>

  <text class="title-line title-line--accent" x="53" y="927" font-size="118"
        textLength="703" lengthAdjust="spacingAndGlyphs">AND WHERE YOU MIGHT TOO</text>

  <text class="author-byline" x="400" y="1075" font-size="71" text-anchor="middle">By KT Dorran</text>
</svg>
</body>
</html>
```